NORELO - Webdesign für eine Poolreinigungsfirma
Zielgruppe
Wir sind NORELO, eine junge Poolreinigungsfirma die gerade erst in den Startlöchern sitzt. Wir befinden uns auf der französischen Insel LA RÉUNION und richten uns an Personen jeglichen Alters, die einen Pool besitzen.
Aufgabenstellung
Wir wünschen uns ein in erster Linie LUXURIÖSES, schickes und sehr ansprechendes Webdesign, dass - unbedingt - die Verbindung zur Natur zeigt (Tropen, Beispielfotos im Anhang). Natur + Wasser / Pool.
BITTE KEINE TYPISCHE POOLWEBSITE, da wir u.a. auch bald in den Verkauf luxuriöser Accessoires gehen möchten. Wir möchten uns von der Konkurrenz stark und deutlich abheben.
Wir wünschen uns einen DUNKLEN MOOD (gerne auch schwarz auf weißem Hintergrund o.ä. ?).
Wir sind von AI-Bildern sehr angetan, da sie Träume erwecken und in der Tiefe ansprechen können. Nutzen Sie diese gerne, bieten Sie uns Vorschläge. Bitte passend zu den Tropen.
Wir überlassen Ihnen vertrauensvoll die Erstellung des Designs der Website (Aufbau, etc), wir möchten uns überraschen lassen.
Unser Logo, ein Briefing für drei gewünschte Seiten und Beispielbilder, die sehr gerne genutzt werden können (oder in Anlehnung an diese, gleicher Stil) sind im Anhang zu finden.
Die Seite sollte unbedingt - auch - die Nutzung mit Mobiltelefonen ermöglichen und keine Verzögerungen beim Aufrufen / Laden der Website aufzeigen.

```html
<!DOCTYPE html>
<html lang="fr">
<head>
<meta charset="utf-8">
<title>NORELO – Entretien de piscine</title>
<link href="https://fonts.googleapis.com/css2?family=Poppins:wght@400;500;600;700&display=swap" rel="stylesheet">
<style>
  :root {
    --ink: #263a45;
    --white: #ffffff;
    --blue: #3597d6;
    --green: #4bbd5c;
    --panel: #efefef;
    --footer: #2e4551;
    --footer-deep: #293e49;
    --footer-field: #3f5763;
    --muted: #d6dee2;
    --ring: #c8cdd0;
  }
  * { box-sizing: border-box; margin: 0; padding: 0; }
  html, body { width: 1200px; height: 2455px; overflow: hidden; }
  body { position: relative; font-family: "Poppins", sans-serif; color: var(--ink); background: var(--white); }
  .abs { position: absolute; }
  a { text-decoration: none; color: inherit; }
  .btn {
    position: absolute; display: flex; align-items: center; justify-content: center; gap: 6px;
    height: 40px; border-radius: 20px; color: var(--white); font-size: 12.5px; font-weight: 500;
    background: linear-gradient(90deg, var(--blue), var(--green));
  }

  /* hero */
  .hero { left: 0; top: 0; width: 1200px; height: 588px;
    background: radial-gradient(ellipse at 72% 40%, #c9a48c 0%, #8fb7c9 28%, transparent 55%),
                linear-gradient(120deg, #5f8fa6 0%, #8fb3c2 30%, #a8cfe0 55%, #3f8fb3 80%, #2b6f93 100%); }
  .nav-link { position: absolute; top: 34px; color: var(--white); font-size: 13.5px; font-weight: 500; }
  .nav-link.active { border-bottom: 2px solid var(--white); padding-bottom: 3px; }
  .brand { left: 500px; top: 18px; width: 200px; display: flex; flex-direction: column; align-items: center; gap: 6px; color: var(--white); }
  .brand-dot { width: 30px; height: 30px; border-radius: 50%; border: 2px solid var(--white); display: block; }
  .brand-name { font-size: 21px; font-weight: 400; letter-spacing: 5px; }
  .hero-title { left: 135px; top: 199px; color: var(--white); font-size: 41px; line-height: 47px; font-weight: 700; }
  .hero-region { left: 135px; top: 357px; color: var(--white); font-size: 14px; }
  .hero-more { left: 135px; top: 415px; color: var(--white); font-size: 12.5px; font-weight: 500; border-bottom: 1.5px solid var(--white); padding-bottom: 3px; }

  .section-title { font-weight: 700; text-transform: uppercase; text-align: center; color: var(--ink); font-size: 30px; line-height: 40px; }
  .lead { text-align: center; font-size: 14px; line-height: 24px; }

  .care-title { left: 300px; top: 656px; width: 600px; }
  .care-lead { left: 250px; top: 750px; width: 700px; }

  .exp-frame { left: 135px; top: 864px; width: 261px; height: 317px; background: linear-gradient(90deg, var(--blue) 30%, var(--green)); }
  .exp-photo { left: 177px; top: 906px; width: 334px; height: 364px; border-top-left-radius: 42px;
    background: linear-gradient(150deg, #3b5a34 0%, #8b7356 35%, #2b9db6 60%, #6e5a44 100%); }
  .exp-title { left: 610px; top: 988px; font-size: 24px; font-weight: 700; text-transform: uppercase; }
  .exp-text { left: 610px; top: 1026px; width: 380px; font-size: 14px; line-height: 24px; }
  .arrow-btn { position: absolute; top: 1171px; width: 37px; height: 37px; border-radius: 50%; border: 1px solid var(--ring); display: flex; align-items: center; justify-content: center; }
  .arrow-btn.on { border-color: var(--ink); }

  .respect-title { left: 336px; top: 1396px; width: 500px; }
  .respect-lead { left: 336px; top: 1486px; width: 508px; }

  .collab-panel { left: 135px; top: 1711px; width: 586px; height: 317px; background: var(--panel); }
  .collab-photo { left: 721px; top: 1668px; width: 344px; height: 394px;
    background: linear-gradient(170deg, #1f3b22 0%, #2f5a33 40%, #1e8b95 70%, #2cb0b8 100%); }
  .collab-title { left: 188px; top: 1770px; font-size: 24px; line-height: 27px; font-weight: 700; text-transform: uppercase; }
  .collab-text { left: 188px; top: 1835px; width: 480px; font-size: 13.8px; line-height: 23.5px; }

  .footer { left: 0; top: 2162px; width: 1200px; height: 293px; background: var(--footer); color: var(--white); }
  .footer-bottom { left: 0; top: 247px; width: 1200px; height: 46px; background: var(--footer-deep); display: flex; align-items: center; justify-content: center; font-size: 13.5px; color: var(--muted); }
  .signup { left: 61px; top: 46px; font-size: 15.5px; }
  .field { left: 61px; top: 76px; width: 296px; height: 40px; border-radius: 4px; background: var(--footer-field); display: flex; align-items: center; justify-content: space-between; padding: 0 12px 0 14px; font-size: 13.5px; }
  .follow { left: 61px; top: 163px; font-size: 13px; color: var(--muted); }
  .social { top: 188px; display: flex; align-items: center; gap: 5px; font-size: 12px; }
  .social-dot { width: 18px; height: 18px; border: 2px solid var(--white); border-radius: 50%; display: block; }
  .col { top: 56px; display: flex; flex-direction: column; gap: 13px; font-size: 13.5px; color: var(--muted); }
  .col-head { color: var(--white); font-weight: 600; font-size: 14px; }
</style>
</head>
<body>
  <section class="hero abs" role="img" aria-label="Photo d'une personne flottant dans l'eau turquoise d'une piscine"></section>
  <nav>
    <a class="nav-link active" style="left:135px" href="#">Home</a>
    <a class="nav-link" style="left:195px" href="#">à propos de nous</a>
    <a class="nav-link" style="left:845px" href="#">Prestations de service</a>
    <a class="nav-link" style="left:1011px" href="#">Contact</a>
  </nav>
  <div class="brand abs"><span class="brand-dot"></span><span class="brand-name">NORELO</span></div>

  <h1 class="hero-title abs">NORELO<br>L’ENTRETIEN DE<br>VOTRE PISCINE</h1>
  <p class="hero-region abs">Secteur Ouest de La Réunion</p>
  <a class="hero-more abs" href="#">apprendre encore plus</a>
  <a class="btn" style="left:290px;top:405px;width:138px;" href="#">Request a Quote</a>

  <section class="care">
    <h2 class="section-title care-title abs">Entretien et<br>nettoyage piscine</h2>
    <p class="lead care-lead abs">Parce que l’entretien et le nettoyage d’une piscine nécessitent de réelles connaissances,<br>choisir un contrat d’entretien de NORELO c’est la certitude d’un service haut de gamme</p>
  </section>

  <section class="exp">
    <div class="exp-frame abs"></div>
    <div class="exp-photo abs" role="img" aria-label="Vue aérienne d'une piscine tropicale entourée de palmiers et de paillotes"></div>
    <h3 class="exp-title abs">Expériences</h3>
    <p class="exp-text abs">Riche d’une expérience de 20 ans, nous nous adressons aux particuliers, professionnels, location</p>
    <a class="btn" style="left:610px;top:1099px;width:167px;" href="#">Demander un devis
      <svg width="9" height="9" viewBox="0 0 10 10"><path d="M2 8L8 2M3 2h5v5" fill="none" stroke="#fff" stroke-width="1.3"/></svg></a>
    <span class="arrow-btn" style="left:610px"><svg width="18" height="10" viewBox="0 0 18 10"><path d="M17 5H1M5 1L1 5l4 4" fill="none" stroke="#263a45" stroke-width="1.3"/></svg></span>
    <span class="arrow-btn on" style="left:657px"><svg width="18" height="10" viewBox="0 0 18 10"><path d="M1 5h16M13 1l4 4-4 4" fill="none" stroke="#263a45" stroke-width="1.3"/></svg></span>
  </section>

  <section class="respect">
    <h2 class="section-title respect-title abs">Respect de votre santé<br>et de l’environnement</h2>
    <p class="lead respect-lead abs">Nous réduisons le nombre de produits chimiques pour un respect maximal de la santé des baigneurs et de l’environnement.</p>
  </section>

  <section class="collab">
    <div class="collab-panel abs"></div>
    <div class="collab-photo abs" role="img" aria-label="Deux personnes au bord d'une piscine entourée de végétation tropicale"></div>
    <h3 class="collab-title abs">Collaborations avec<br>nos partenaires</h3>
    <p class="collab-text abs">En cas de détection d’un dysfonctionnement par notre équipe, nous vous proposons une intervention par nos partenaires certifiés et professionnels. Pour que vous retrouvez rapidement votre piscine en état de plein fonctionnement.</p>
    <a class="btn" style="left:188px;top:1954px;width:149px;" href="#">Request a Quote
      <svg width="9" height="9" viewBox="0 0 10 10"><path d="M2 8L8 2M3 2h5v5" fill="none" stroke="#fff" stroke-width="1.3"/></svg></a>
  </section>

  <footer class="footer abs">
    <p class="signup abs">Inscription à la newsletter !</p>
    <div class="field abs"><span>E-Mail</span><svg width="12" height="9" viewBox="0 0 12 9"><path d="M1 4.5h10M7.5 1L11 4.5 7.5 8" fill="none" stroke="#fff" stroke-width="1.3"/></svg></div>
    <p class="follow abs">Suivez-nous:</p>
    <span class="social abs" style="left:61px"><span class="social-dot"></span>Picta</span>
    <span class="social abs" style="left:120px"><span class="social-dot"></span>Amicio</span>
    <div class="col abs" style="left:675px"><span class="col-head">Pages</span><span>Home</span><span>About Us</span><span>Services</span><span>Contact</span></div>
    <div class="col abs" style="left:793px"><span class="col-head">Service</span><span>Newsletter</span><span>FAQ</span><span>Service après vente</span></div>
    <div class="col abs" style="left:982px"><span class="col-head">Légal</span><span>imprimer</span><span>Protection des données</span><span>Droit de rétractation</span><span>Conditions</span></div>
    <div class="footer-bottom abs">© 2023 Norelo</div>
  </footer>
</body>
</html>
```